Post storm repair flyer

looking for an eye catching 6x9 postcard to send out to single family home owners advertising a "Post Storm Repair Special" explaining that after the recent hurricanes its very important to have your roof checked and any repairs fixed right away before they become a bigger more costly problem and that even though your home wasn't directly hit by the storm the high wind gust could've cause unseen damage.
offer $200 off any repair *some rules may apply
Lark Roofing
888.417.LARK
www.LarkRoofing.example

Roofing

```html
<!DOCTYPE html>
<html lang="en">
<head>
<meta charset="utf-8">
<title>Lark Roofing – Post Storm Repair Special</title>
<link rel="stylesheet" href="https://fonts.googleapis.com/css2?family=Roboto:ital,wght@0,400;0,700;0,900;1,700&family=Roboto+Condensed:ital,wght@0,700;1,400;1,700&family=Montserrat:wght@500&family=Yellowtail&display=swap">
<style>
  :root {
    --gold: #f4b11c;
    --gold-pale: #f9e6bd;
    --ink: #0b0b0b;
    --white: #ffffff;
    --grey-text: #5e5e5e;
    --body-text: #1f1f1f;
    --stage: #e2e2e2;
    --hot-red: #e8202a;
    --hot-orange: #f7941d;
  }
  html, body {
    margin: 0;
    width: 1200px;
    height: 1200px;
    overflow: hidden;
    background: var(--stage);
  }
  .postcard {
    position: absolute;
    left: 30px;
    top: 220px;
    width: 1562px;
    height: 1042px;
    transform: scale(0.7298);
    transform-origin: 0 0;
    background: var(--white);
    overflow: hidden;
    font-family: "Roboto", sans-serif;
  }
  .postcard-shapes { position: absolute; inset: 0; }
  .postcard > div, .postcard > p { position: absolute; margin: 0; line-height: 1; }

  .headline {
    left: 96px;
    font-weight: 900;
    font-size: 112px;
    color: var(--ink);
    letter-spacing: -1px;
  }
  .headline-top { top: 48px; }
  .headline-mid { top: 158px; }
  .headline-script {
    left: 112px;
    top: 238px;
    font-family: "Yellowtail", cursive;
    font-size: 150px;
    color: var(--white);
    transform: rotate(-7deg);
    transform-origin: left center;
  }

  .brand-name {
    left: 480px;
    top: 300px;
    width: 350px;
    display: flex;
    align-items: center;
    justify-content: center;
    gap: 14px;
    font-weight: 700;
    font-size: 46px;
    color: var(--ink);
  }
  .brand-dot {
    width: 26px;
    height: 26px;
    border-radius: 50%;
    background: var(--ink);
  }
  .brand-web {
    left: 405px;
    top: 446px;
    width: 500px;
    text-align: center;
    font-family: "Montserrat", sans-serif;
    font-weight: 500;
    font-size: 36px;
    letter-spacing: 1.5px;
    color: #2b2b2b;
  }

  .offer-amount {
    left: 70px;
    top: 512px;
    width: 300px;
    text-align: center;
    font-family: "Roboto Condensed", sans-serif;
    font-weight: 700;
    font-size: 118px;
    color: var(--gold);
  }
  .offer-amount sup { font-size: 52px; vertical-align: 48px; margin-right: 4px; }
  .offer-off {
    left: 108px;
    top: 612px;
    display: flex;
    align-items: center;
    gap: 6px;
    font-family: "Roboto Condensed", sans-serif;
    font-weight: 700;
    color: var(--white);
  }
  .offer-off-word { font-size: 74px; }
  .offer-off-scope { font-size: 33px; line-height: 0.92; }
  .offer-terms {
    left: 70px;
    top: 700px;
    width: 300px;
    text-align: center;
    font-family: "Roboto Condensed", sans-serif;
    font-style: italic;
    font-size: 18px;
    line-height: 1.05;
    color: var(--gold);
  }
  .call-us {
    left: 125px;
    top: 812px;
    width: 190px;
    text-align: center;
    font-family: "Roboto Condensed", sans-serif;
    font-weight: 700;
    font-style: italic;
    font-size: 64px;
    line-height: 0.95;
    color: var(--white);
  }

  .benefit {
    left: 447px;
    font-weight: 700;
    font-size: 64px;
    color: var(--ink);
  }
  .benefit-one { top: 535px; }
  .benefit-two { top: 617px; }

  .pitch {
    left: 447px;
    top: 712px;
    font-size: 25px;
    line-height: 34px !important;
    color: var(--body-text);
  }
  .pitch-emphasis {
    left: 447px;
    top: 780px;
    font-weight: 700;
    font-style: italic;
    font-size: 28px;
    line-height: 39px !important;
    color: var(--gold);
  }
  .fine-print {
    left: 447px;
    top: 896px;
    font-size: 17.5px;
    line-height: 22px !important;
    color: var(--grey-text);
  }

  .phone-number {
    left: 913px;
    top: 893px;
    font-family: "Roboto Condensed", sans-serif;
    font-style: italic;
    font-weight: 400;
    font-size: 104px;
    color: var(--gold);
    letter-spacing: 1px;
  }
  .phone-number span { color: var(--white); }
</style>
</head>
<body>
<main class="postcard">
  <svg class="postcard-shapes" viewBox="0 0 1562 1042" width="1562" height="1042">
    <defs>
      <linearGradient id="storm-photo" x1="0" y1="0" x2="1" y2="1">
        <stop offset="0" stop-color="#6e9a4a"/>
        <stop offset="0.35" stop-color="#a9b2ae"/>
        <stop offset="0.65" stop-color="#b98d52"/>
        <stop offset="1" stop-color="#5f7d7a"/>
      </linearGradient>
      <linearGradient id="call-fill" x1="1" y1="0" x2="0" y2="1">
        <stop offset="0" stop-color="var(--hot-red)"/>
        <stop offset="0.7" stop-color="var(--hot-orange)"/>
      </linearGradient>
    </defs>

    <polygon class="gold-field" points="0,0 1060,0 0,655" fill="var(--gold)"/>
    <line class="gold-stripe" x1="0" y1="700" x2="560" y2="352" stroke="var(--gold)" stroke-width="13"/>
    <line class="gold-stripe" x1="0" y1="958" x2="380" y2="727" stroke="var(--gold)" stroke-width="13"/>
    <rect class="gold-base" x="0" y="1021" width="720" height="21" fill="var(--gold)"/>

    <polygon class="storm-photo" role="img" aria-label="Aerial photo of a storm-damaged house roof with missing shingles and exposed rafters"
      points="1000,0 1562,0 1562,867 765,867 1010,262 868,300 958,60" fill="url(#storm-photo)"/>
    <polygon class="lightning-bolt" points="968,0 1010,0 905,268 1022,248 872,800 992,302 878,334" fill="var(--white)"/>

    <polygon class="phone-band" points="765,867 1562,867 1562,1042 700,1042" fill="var(--ink)"/>

    <polygon class="ghost-hex" points="105,740 187,787 187,882 105,930 23,882 23,787" fill="none" stroke="var(--gold-pale)" stroke-width="3"/>
    <polygon class="ghost-hex" points="350,785 422,827 422,910 350,952 278,910 278,827" fill="none" stroke="var(--gold-pale)" stroke-width="3"/>

    <polygon class="offer-hex" points="220,435 363,518 363,683 220,765 77,683 77,518" fill="var(--ink)"/>
    <polygon class="offer-hex-rim" points="220,446 353,524 353,677 220,754 87,677 87,524" fill="none" stroke="#7a7a7a" stroke-width="1.5"/>
    <line class="offer-rule" x1="85" y1="692" x2="355" y2="692" stroke="var(--gold)" stroke-width="1.5"/>

    <polygon class="call-hex" points="220,755 315,810 315,920 220,975 125,920 125,810" fill="url(#call-fill)"/>

    <polygon class="wind-hex" points="399,908 427,924 427,956 399,972 371,956 371,924" fill="var(--gold)"/>
    <path class="wind-lines" d="M380 934 q14 -8 28 0 t14 0 M383 944 q14 -8 28 0 M386 954 q12 -6 24 0" fill="none" stroke="var(--white)" stroke-width="2" stroke-linecap="round"/>

    <line class="list-rule" x1="405" y1="523" x2="815" y2="523" stroke="var(--gold-pale)" stroke-width="2"/>
    <line class="list-rule" x1="405" y1="605" x2="815" y2="605" stroke="var(--gold-pale)" stroke-width="2"/>
    <line class="list-rule" x1="405" y1="692" x2="815" y2="692" stroke="var(--gold-pale)" stroke-width="2"/>

    <g class="tick" transform="translate(418,568)">
      <circle r="11" fill="none" stroke="var(--gold)" stroke-width="4"/>
      <path d="M-6 0 l5 6 l12 -16" fill="none" stroke="var(--gold)" stroke-width="4" stroke-linecap="round"/>
    </g>
    <g class="tick" transform="translate(418,650)">
      <circle r="11" fill="none" stroke="var(--gold)" stroke-width="4"/>
      <path d="M-6 0 l5 6 l12 -16" fill="none" stroke="var(--gold)" stroke-width="4" stroke-linecap="round"/>
    </g>

    <g class="phone-icon" transform="translate(842,945)">
      <polygon points="0,-50 43,-25 43,25 0,50 -43,25 -43,-25" fill="none" stroke="var(--gold)" stroke-width="4"/>
      <path d="M-17 -15 c-4 4 -3 12 6 22 c9 9 18 11 22 7 l4 -5 l-9 -8 l-5 4 c-4 -2 -8 -6 -10 -10 l4 -5 l-8 -9 z" fill="var(--gold)"/>
      <path d="M3 -16 a14 14 0 0 1 14 14 M3 -26 a24 24 0 0 1 24 24" fill="none" stroke="var(--gold)" stroke-width="3.5" stroke-linecap="round"/>
    </g>
  </svg>

  <div class="headline headline-top">Post Storm</div>
  <div class="headline headline-mid">Repair</div>
  <div class="headline-script">Special</div>

  <div class="brand-name"><span class="brand-dot"></span>Lark Roofing</div>
  <div class="brand-web">LARKROOFING.EXAMPLE</div>

  <div class="offer-amount"><sup>$</sup>200</div>
  <div class="offer-off"><span class="offer-off-word">OFF</span><span class="offer-off-scope">ANY<br>REPAIR</span></div>
  <p class="offer-terms">*some rules may<br>apply</p>
  <div class="call-us">CALL<br>US</div>

  <div class="benefit benefit-one">Roof checked</div>
  <div class="benefit benefit-two">Roof repairs</div>
  <p class="pitch">after the recent hurricanes<br>before they become</p>
  <p class="pitch-emphasis">MORE COSTLY<br>PROBLEM.</p>
  <p class="fine-print">even though your home wasn’t<br>directly hit by the storm The<br>high wind gust could’ve cause<br>unseen damage.</p>

  <div class="phone-number">888.417.<span>LARK</span></div>
</main>
</body>
</html>
```